"Thank You" flyer design

We need a "thank you" flyer that will be sent out with all our products.
a6 size landscape,
We manufacture personalised shaped signs.
I've attached a rough idea of what we are after, but would like it to be improved upon with some artistic flare..

Side one - We would like the flyer to have a simple message - "thank you for shopping with us"

Side two - we would also like our logo and a union jack made in the UK badge and our address and contact details with our website www.lumkinprints.co.uk being the most prominent..

We are after a simple bold design what would be printed on a small a6 card that people might hopefully want to keep, so the end design needs to be pretty cool.

Industry/Entity Type

Shopping

Font styles to use
Serif
Sans Serif

```html
<!DOCTYPE html>
<html lang="en">
<head>
<meta charset="utf-8">
<title>Lumkin Prints – Thank You Flyer</title>
<link rel="stylesheet" href="https://fonts.googleapis.com/css2?family=Fira+Sans:wght@300;400;700;900&display=swap">
<style>
  :root {
    --stage: #000000;
    --magenta: #d9147e;
    --ink: #111111;
    --white: #ffffff;
    --navy: #26357a;
    --sepia-light: #f4e2c6;
    --sepia-mid: #dcc6a4;
    --sepia-dark: #b9a587;
    --flag-cream: #f3ebe4;
    --flag-blue: #b9c3dc;
    --flag-pink: #ecc3cf;
  }
  html, body {
    margin: 0;
    padding: 0;
    width: 1200px;
    height: 1200px;
    overflow: hidden;
    background: var(--stage);
    font-family: "Fira Sans", Arial, sans-serif;
  }
  .sheet {
    position: relative;
    width: 1200px;
    height: 1200px;
  }
  .card {
    position: absolute;
    left: 156px;
    width: 641px;
    height: 453px;
    overflow: hidden;
  }
  .card--front { top: 99px; }
  .card--back  { top: 647px; }

  .card__backdrop {
    position: absolute;
    inset: 0;
  }
  .card--front .card__backdrop {
    background:
      radial-gradient(ellipse at 30% 30%, rgba(255,255,255,0.45), transparent 60%),
      linear-gradient(180deg, var(--sepia-light) 0%, var(--sepia-mid) 55%, var(--sepia-dark) 80%, var(--sepia-light) 100%);
  }
  .card--back .card__backdrop {
    background:
      linear-gradient(180deg, transparent 38%, var(--flag-pink) 40%, var(--flag-pink) 58%, transparent 60%),
      linear-gradient(135deg, var(--flag-blue) 0%, var(--flag-cream) 35%, var(--flag-cream) 65%, var(--flag-blue) 100%);
  }

  .line {
    position: absolute;
    left: 0;
    right: 0;
    margin: 0;
    text-align: center;
    line-height: 1;
    white-space: nowrap;
  }
  .headline {
    top: 158px;
    font-size: 86px;
    font-weight: 900;
    color: var(--magenta);
    -webkit-text-stroke: 3px var(--white);
    paint-order: stroke fill;
    text-shadow: 3px 4px 4px rgba(0,0,0,0.35);
    letter-spacing: 1px;
  }
  .subhead {
    top: 254px;
    font-size: 40px;
    font-weight: 400;
    color: var(--ink);
  }
  .visit-label {
    font-size: 18px;
    font-weight: 400;
    color: var(--ink);
  }
  .card--front .visit-label { top: 343px; }
  .front-url {
    top: 373px;
    font-size: 27px;
    font-weight: 300;
    color: var(--magenta);
    letter-spacing: 0.5px;
  }

  .card--back .visit-label {
    top: 62px;
    font-size: 20px;
    color: var(--magenta);
  }
  .back-url {
    top: 92px;
    font-size: 37px;
    font-weight: 700;
    color: var(--ink);
  }
  .tagline {
    top: 146px;
    font-size: 20px;
    color: var(--ink);
  }
  .brand {
    top: 212px;
    font-size: 36px;
    font-weight: 700;
    color: var(--magenta);
  }
  .callout-label {
    top: 319px;
    font-size: 20px;
    color: var(--magenta);
  }
  .phone {
    top: 350px;
    font-size: 62px;
    font-weight: 700;
    color: var(--ink);
  }
  .address {
    top: 424px;
    font-size: 15px;
    font-weight: 400;
    color: var(--ink);
  }
  .uk-badge {
    position: absolute;
    top: 20px;
    right: 20px;
    width: 64px;
    height: 64px;
  }

  .marker {
    position: absolute;
    left: 833px;
    display: flex;
    align-items: center;
    gap: 20px;
  }
  .marker--front { top: 277px; }
  .marker--back  { top: 827px; }
  .marker__label {
    color: var(--white);
    font-size: 29px;
    font-weight: 400;
  }
</style>
</head>
<body>
<main class="sheet">

  <section class="card card--front">
    <div class="card__backdrop" role="img" aria-label="Faded sepia photograph of a city street with black taxis and terraced buildings"></div>
    <h1 class="line headline">THANK YOU</h1>
    <p class="line subhead">FOR SHOPPING WITH US</p>
    <p class="line visit-label">Please visit</p>
    <p class="line front-url">WWW.LUMKINPRINTS.CO.UK</p>
  </section>

  <div class="marker marker--front">
    <svg width="47" height="96" viewBox="0 0 47 96" aria-hidden="true">
      <polygon points="0,48 47,0 47,96" fill="var(--magenta)"/>
    </svg>
    <span class="marker__label">Front</span>
  </div>

  <section class="card card--back">
    <div class="card__backdrop" role="img" aria-label="Faded, weathered Union Jack flag background"></div>
    <svg class="uk-badge" viewBox="0 0 64 64" role="img" aria-label="Made in the UK badge">
      <circle cx="32" cy="32" r="30" fill="var(--navy)" stroke="var(--white)" stroke-width="3"/>
    </svg>
    <p class="line visit-label">Please visit</p>
    <p class="line back-url">www.lumkinprints.co.uk</p>
    <p class="line tagline">For personalised shaped signs</p>
    <p class="line brand">Lumkin Prints</p>
    <p class="line callout-label">CALL OUT TEAM ON</p>
    <p class="line phone">01632 960418</p>
    <p class="line address">Unit 4, Mill Lane, Northwich CW9 5QT</p>
  </section>

  <div class="marker marker--back">
    <svg width="47" height="96" viewBox="0 0 47 96" aria-hidden="true">
      <polygon points="0,48 47,0 47,96" fill="var(--magenta)"/>
    </svg>
    <span class="marker__label">Back</span>
  </div>

</main>
</body>
</html>
```